Redesign our current site www.lendvoro.com into a html5 design

We are a better option for people who need a unsecured loan. We have built our business on offering lower more affordable loans then the competition. Our website is old school and needs a bolder/fresher look. I don't want to lose our content and you must keep the disclosures.
Please make sure to keep our testimonials and the short application on the upper left hand side of the page. Also, we need to have the disclosures at the bottom. You can change the testimonial pictures with better HD pics. An example of this is tamberfinance.com

Reason: Due to the weekend we were unable to get as many designs as we hoped. We are extending the project one day. Thank you for your patience.

Target Market(s)

quillfund.com; morvalend.com; zephloan.com
people that need a better loan option and a lower interest rate.

Industry/Entity Type

School

Requirements
Must have
• Html5 and take the three tabs and make that the main html 5 page. Then take the top headers and make them separate pages.

```html
<!DOCTYPE html>
<html lang="en">
<head>
<meta charset="utf-8">
<title>Lendvoro Financial – A Better Personal Loan</title>
<link href="https://fonts.googleapis.com/css2?family=Ubuntu:ital,wght@0,300;0,400;0,500;0,700;1,400&display=swap" rel="stylesheet">
<style>
:root{
  --green:#62cc35;
  --green-text:#3fb31d;
  --lime:#ccff66;
  --dark:#203029;
  --charcoal:#2f2f2f;
  --grey-bar:#cfcfcf;
  --badge:#e9eee4;
  --ink:#555;
  --body:#6d6d6d;
  --white:#fff;
}
*{margin:0;padding:0;box-sizing:border-box}
html,body{width:1200px;height:935px;overflow:hidden;background:var(--white);font-family:"Ubuntu",sans-serif}
.page{position:relative;width:1200px;height:935px}
.brand{position:absolute;left:205px;top:30px;display:flex;align-items:center;gap:8px;font-size:24px;font-weight:500;color:var(--charcoal)}
.brand-dot{width:14px;height:14px;border-radius:50%;background:var(--green)}
.call{position:absolute;left:758px;top:0;width:266px;height:33px;background:var(--green);color:var(--white);font-size:14px;display:flex;align-items:center;justify-content:center;clip-path:polygon(0 0,100% 0,95% 100%,5% 100%)}
.nav{position:absolute;top:67px;right:181px;display:flex;gap:27px;list-style:none;font-size:12px;color:var(--ink);letter-spacing:.3px}
.hero-band{position:absolute;left:0;top:106px;width:1200px;height:408px;background:var(--dark)}
.hero-photo{position:absolute;left:446px;top:106px;width:754px;height:408px;background:linear-gradient(135deg,#8a9893 0%,#5d6d67 45%,#33423c 100%)}
.form-panel{position:absolute;left:170px;top:99px;width:276px;height:423px;background:var(--green)}
.form-title{position:absolute;left:31px;top:33px;color:var(--white);font-size:17px;font-weight:300;letter-spacing:.4px}
.form-title b{font-weight:700}
.field{position:absolute;left:32px;width:212px;height:35px;background:var(--lime);color:#4a5a20;font-size:12px;padding:0 14px;display:flex;align-items:center;justify-content:space-between}
.field-caret{width:0;height:0;border-left:5px solid transparent;border-right:5px solid transparent;border-top:6px solid var(--charcoal)}
.cash-btn{position:absolute;left:31px;top:307px;width:117px;height:42px;background:var(--charcoal);color:var(--white);font-size:12px;font-weight:500;display:flex;align-items:center;justify-content:center}
.secure-badge{position:absolute;left:172px;top:306px;width:66px;height:40px;background:var(--badge);border-radius:4px}
.testimonial{position:absolute;left:446px;top:378px;width:583px;height:94px;background:rgba(40,48,45,.78);padding:21px 27px;color:var(--white)}
.testimonial p{font-size:13px;line-height:17px;letter-spacing:.1px}
.testimonial cite{display:block;margin-top:3px;font-size:11.5px;color:var(--green)}
.why-tab{position:absolute;left:170px;top:582px;width:299px;height:102px;background:var(--green);color:var(--white);padding:31px 14px;font-size:17px;line-height:21px;font-weight:300}
.why-tab b{font-weight:700}
.why-tab::after{content:"";position:absolute;right:0;top:40px;border-top:11px solid transparent;border-bottom:11px solid transparent;border-right:14px solid var(--white)}
.side-link{position:absolute;left:184px;font-size:17px;line-height:21px;font-weight:300;color:var(--green-text)}
.side-link b{display:block;font-weight:700;color:#666}
.promo-bar{position:absolute;left:501px;top:582px;width:528px;height:50px;display:flex}
.promo-text{flex:0 0 327px;background:var(--grey-bar);color:var(--ink);font-size:14px;display:flex;align-items:center;padding-left:20px}
.promo-cta{flex:1;background:var(--green);color:var(--white);font-size:14px;display:flex;align-items:center;justify-content:center}
.benefit{position:absolute;left:501px;width:528px}
.benefit svg{position:absolute;left:2px;top:0}
.benefit h3{margin-left:79px;font-size:12.5px;font-weight:400;color:var(--green-text);letter-spacing:.3px}
.benefit p{margin:6px 10px 0 79px;font-size:11.5px;line-height:17px;color:var(--body);font-weight:300;text-align:justify}
</style>
</head>
<body>
<div class="page">
  <header>
    <div class="brand"><span class="brand-dot"></span>Lendvoro Financial</div>
    <div class="call">CALL NOW&nbsp; 1-855-555-0142</div>
    <ul class="nav"><li>HOME</li><li>RATES/TERMS/LICENCES</li><li>CONTACT US</li><li>MY ACCOUNT</li></ul>
  </header>

  <section>
    <div class="hero-band"></div>
    <div class="hero-photo" role="img" aria-label="Young man in a hoodie sitting in front of a chain-link fence"></div>
    <form class="form-panel">
      <h2 class="form-title">GET STARTED <b>TODAY</b></h2>
      <div class="field" style="top:72px">First Name</div>
      <div class="field" style="top:118px">First Name</div>
      <div class="field" style="top:162px">Email Address</div>
      <div class="field" style="top:207px">Phone Number</div>
      <div class="field" style="top:252px">State<span class="field-caret"></span></div>
      <div class="cash-btn">GET CASH NOW</div>
      <div class="secure-badge" role="img" aria-label="Security certificate badge"></div>
    </form>
    <blockquote class="testimonial">
      <p>I was able to avoid bank NSF fees and fix my car's brakes so I didn't miss work.The service was fast and friendly. I recommend them to everyone.</p>
      <cite>- Marcus , Frieght and Delivery Driver</cite>
    </blockquote>
  </section>

  <aside>
    <div class="why-tab">WHY LENDVORO<br><b>FINANCIAL?</b></div>
    <div class="side-link" style="top:719px">HOW DOES<b>IT WORK ?</b></div>
    <div class="side-link" style="top:815px">LENDVORO VS<b>BANK /LATE FEES</b></div>
  </aside>

  <main>
    <div class="promo-bar"><div class="promo-text">OUR LOANS ARE BETTER THAN PAYDAY.</div><div class="promo-cta">GET APPROVED NOW</div></div>

    <div class="benefit" style="top:657px">
      <svg width="60" height="48" viewBox="0 0 60 48" fill="#2f2f2f">
        <ellipse cx="12" cy="38" rx="11" ry="5"/><ellipse cx="12" cy="31" rx="11" ry="5"/><ellipse cx="12" cy="24" rx="11" ry="5"/>
        <ellipse cx="35" cy="26" rx="10" ry="4.5"/><ellipse cx="35" cy="19" rx="10" ry="4.5"/><ellipse cx="35" cy="12" rx="10" ry="4.5"/><ellipse cx="35" cy="5" rx="10" ry="4.5"/>
        <circle cx="47" cy="36" r="10"/><text x="47" y="40" font-size="12" fill="#fff" text-anchor="middle" font-family="Ubuntu,sans-serif" font-weight="700">$</text>
      </svg>
      <h3>GET MORE CASH</h3>
      <p>Typical payday loans offer between $250-$300. With Lendvoro Financial's installment loan you can get up to $1,000 as a first time borrower.</p>
    </div>

    <div class="benefit" style="top:731px">
      <svg width="60" height="56" viewBox="0 0 60 56">
        <rect x="3" y="8" width="54" height="46" rx="2" fill="#2f2f2f"/><rect x="8" y="20" width="44" height="29" fill="#fff"/>
        <rect x="13" y="2" width="5" height="12" fill="#2f2f2f"/><rect x="42" y="2" width="5" height="12" fill="#2f2f2f"/>
        <text x="30" y="45" font-size="22" font-weight="700" text-anchor="middle" fill="#2f2f2f" font-family="Ubuntu,sans-serif">31</text>
      </svg>
      <h3>PAY OVER TIME</h3>
      <p>Loans are paid back over a 6-9 month period keeping your payments affordable. Maximum loan amount for initial loan is $1,000.00. Refer to Rates/Terms/Licenses for additional details. Complete disclosures of APR, fees and payment terms are provided within the Loan Agreement.</p>
    </div>

    <div class="benefit" style="top:840px">
      <svg width="60" height="60" viewBox="0 0 60 60" fill="#2f2f2f">
        <path d="M22 4h16l-5 10h-6z"/><path d="M26 16h8c14 8 22 20 22 30 0 8-8 12-26 12S4 54 4 46c0-10 8-22 22-30z"/>
        <text x="30" y="48" font-size="22" font-weight="700" text-anchor="middle" fill="#fff" font-family="Ubuntu,sans-serif">$</text>
      </svg>
      <h3>SAVE MONEY</h3>
      <p>Our interest rate is typically 40-70% less than a payday lender's and will save you costly NSF and other late fees.1</p>
    </div>
  </main>
</div>
</body>
</html>
```